Orvane Slab Hub

- Brochure design

Target Market(s)

Granite and Quartz

Font styles to use
Sans Serif

Colors

Designer to choose colors to be used in the design.

Requirements
Must have
• I post the instruction file below
Nice to have
Should not have

```html
<!DOCTYPE html>
<html lang="en">
<head>
<meta charset="utf-8">
<title>Orvane Slab Hub – Quartz Brochure</title>
<link href="https://fonts.googleapis.com/css2?family=PT+Sans+Narrow:wght@400;700&display=swap" rel="stylesheet">
<style>
  :root {
    --bg: #f4f4f4;
    --paper: #ffffff;
    --paper-right: #f7f7f7;
    --band: #2f2927;
    --band-line: #e9e6e4;
    --ink: #2a2a2a;
    --ink-light: #ffffff;
    --overlay: rgba(60, 56, 54, 0.78);
  }
  * { box-sizing: border-box; margin: 0; padding: 0; }
  html, body {
    width: 1200px; height: 900px; overflow: hidden;
    background: var(--bg);
    font-family: "PT Sans Narrow", "Arial Narrow", sans-serif;
    color: var(--ink);
  }
  .spread {
    position: absolute; left: 50px; top: 46px;
    width: 1100px; height: 808px;
    display: flex;
    box-shadow: 0 12px 40px rgba(0,0,0,0.12);
  }
  .page { position: relative; width: 550px; height: 808px; overflow: hidden; }
  .page--left { background: var(--paper); border-right: 1px solid #d6d6d6; }
  .page--right { background: var(--paper-right); }

  .page-header {
    position: absolute; left: 0; top: 0; width: 100%; height: 134px;
    background: var(--band);
  }
  .page-header::after {
    content: ""; position: absolute; left: 0; right: 0; top: 112px;
    height: 1px; background: var(--band-line);
  }
  .brand {
    position: absolute; left: 42px; top: 54px; color: var(--ink-light);
  }
  .brand-name { font-size: 30px; font-weight: 400; letter-spacing: 0.5px; line-height: 1; }
  .brand-tagline { font-size: 11px; margin-top: 6px; }
  .section-title {
    position: absolute; right: 34px; top: 66px;
    font-size: 36px; color: var(--ink-light); font-weight: 400; line-height: 1;
  }

  .kitchen-photo {
    position: absolute; left: 0; top: 134px; width: 100%; height: 674px;
    background:
      linear-gradient(180deg, #d9d9d7 0%, #c9c8c5 28%, #a8a39d 45%, #8c7d6d 60%, #9a958f 75%, #b7b3ad 100%);
  }
  .intro-box {
    position: absolute; left: 281px; top: 470px; width: 269px; height: 288px;
    background: var(--overlay); color: var(--ink-light);
    padding: 14px 40px 0 36px;
    font-size: 13.5px; line-height: 17.6px;
  }

  .page-footer {
    position: absolute; bottom: 12px; font-size: 10px; display: flex; align-items: baseline; gap: 10px;
  }
  .page-footer .num { font-size: 15px; }
  .page--left .page-footer { left: 14px; color: var(--ink-light); }
  .page--right .page-footer { right: 12px; color: var(--ink); }

  .swatch-grid {
    position: absolute; left: 37px; top: 158px;
    display: grid; grid-template-columns: repeat(5, 84px);
    column-gap: 14px; row-gap: 0;
    grid-auto-rows: 149px;
  }
  .swatch { text-align: center; font-size: 11.5px; line-height: 13px; }
  .swatch-chip { width: 84px; height: 91px; margin-bottom: 6px; box-shadow: 0 0 0 1px rgba(0,0,0,0.04); }
</style>
</head>
<body>
<div class="spread">
  <section class="page page--left">
    <header class="page-header">
      <div class="brand">
        <div class="brand-name">Orvane Slab Hub</div>
        <div class="brand-tagline">Naturally Beautiful, Premium Quality</div>
      </div>
    </header>
    <div class="kitchen-photo" role="img" aria-label="Photo of a modern kitchen with white gloss cabinets, steel splashback and a grey quartz island"></div>
    <div class="intro-box">
      Lorem ipsum dolor sit amet. Iriure est diam voluptua justo duis diam. Est nonumy et lorem eum. Eros nonummy sea stet eos nostrud sit tempor. Ipsum no justo facilisi. Lorem augue dolores eos takimata kasd sed. Et vero suscipit. Vel veniam dolor exerci est esse luptatum. Lobortis kasd et clita et feugiat sed cum. Dolore eos nulla. Eros dolore eos esse adipiscing sit. Elitr est iriure et consetetur. Magna at in magna labore feugiat. Dolores labore laoreet amet no.
    </div>
    <footer class="page-footer"><span class="num">05</span><span>www.orvaneslabhub.com</span></footer>
  </section>

  <section class="page page--right">
    <header class="page-header">
      <h1 class="section-title">Quartz</h1>
    </header>
    <div class="swatch-grid">
      <div class="swatch"><div class="swatch-chip" role="img" aria-label="White quartz sample with faint grey veins" style="background:linear-gradient(135deg,#f3f3f0,#e6e6e2)"></div>Alba Vena</div>
      <div class="swatch"><div class="swatch-chip" role="img" aria-label="White quartz sample with fine grey veins" style="background:linear-gradient(135deg,#f4f4f6,#dcdce0 55%,#f2f2f4)"></div>Frost Vein</div>
      <div class="swatch"><div class="swatch-chip" role="img" aria-label="Warm light grey quartz sample" style="background:linear-gradient(135deg,#e2e0db,#d6d3ce)"></div>Soft Linen</div>
      <div class="swatch"><div class="swatch-chip" role="img" aria-label="White quartz sample with bold grey veins" style="background:linear-gradient(135deg,#ebe9ed,#cfccd3 50%,#e6e4e8)"></div>Misty Vein</div>
      <div class="swatch"><div class="swatch-chip" role="img" aria-label="Golden speckled quartz sample" style="background:linear-gradient(135deg,#b89a5c,#8f7340)"></div>Golden Grain 1</div>

      <div class="swatch"><div class="swatch-chip" role="img" aria-label="Gold and brown patterned quartz sample" style="background:linear-gradient(135deg,#c98a35,#6e4a26 55%,#d49a4a)"></div>Golden Grain</div>
      <div class="swatch"><div class="swatch-chip" role="img" aria-label="Black sparkle quartz sample" style="background:#161014"></div>Night Spark</div>
      <div class="swatch"><div class="swatch-chip" role="img" aria-label="Dark brown sparkle quartz sample" style="background:linear-gradient(135deg,#56301f,#3f2419)"></div>Spark Dark<br>Brown</div>
      <div class="swatch"><div class="swatch-chip" role="img" aria-label="Light grey sparkle quartz sample" style="background:linear-gradient(135deg,#e5e6e3,#d6d7d3)"></div>Spark Light<br>Grey</div>
      <div class="swatch"><div class="swatch-chip" role="img" aria-label="White sparkle quartz sample" style="background:linear-gradient(135deg,#f3f0ea,#e6e2db)"></div>Spark White</div>

      <div class="swatch"><div class="swatch-chip" role="img" aria-label="Icy white speckled quartz sample" style="background:linear-gradient(135deg,#e2e2e3,#c9c9cb)"></div>Glacier White</div>
      <div class="swatch"><div class="swatch-chip" role="img" aria-label="Solid dark grey quartz sample" style="background:#4b4f4d"></div>Slate Grey</div>
      <div class="swatch"><div class="swatch-chip" role="img" aria-label="Solid taupe brown quartz sample" style="background:#a68f7b"></div>Taupe Brown</div>
      <div class="swatch"><div class="swatch-chip" role="img" aria-label="Light grey veined quartz sample" style="background:linear-gradient(135deg,#d8d8d5,#c2c2bf)"></div>Riverline</div>
      <div class="swatch"><div class="swatch-chip" role="img" aria-label="Grey and white shell pattern quartz sample" style="background:linear-gradient(135deg,#b5b6b4,#5f605f 50%,#c3c4c2)"></div>Shell Mosaic</div>

      <div class="swatch"><div class="swatch-chip" role="img" aria-label="Off-white pebble pattern quartz sample" style="background:linear-gradient(135deg,#e0ded8,#c8c5bd)"></div>Pebble White</div>
      <div class="swatch"><div class="swatch-chip" role="img" aria-label="Plain white quartz sample" style="background:#efefed"></div>Clean White</div>
    </div>
    <footer class="page-footer"><span>www.orvaneslabhub.com</span><span class="num">06</span></footer>
  </section>
</div>
</body>
</html>
```